Lawn mowing business card design

We need a business card design for our lawn mowing and gardening business which is located in the Northern Beaches of Sydney. Our business name is Meadowline Turf and our logo is predominantly green and yellow in color. Please see our website at www.meadowlineturf.com.au for design ideas. The business targets young professionals and older clientele. As such the font should be easy to read, but I also want the business card to be colorful and stand out.

Target Market(s)

young professionals

Industry/Entity Type

Lawn Care

Contact Information for Business Card

Meadowline Turf, Gareth Pellow, 0478559201, www.meadowlineturf.com.au, email: meadowlineturf@mailbox-example.com

Font styles to use
Serif

Colors
9bcb3b
fbed22

Requirements
Must have
• Must include the details listed above. Must include the attached logo.
Nice to have
• Logo attached with two copies. The logo without any writing is high quality, please feel free to be creative with the text stating our business name "Meadowline Turf" using this file.

```html
<!DOCTYPE html>
<html lang="en">
<head>
<meta charset="utf-8">
<title>Meadowline Turf – Business Card</title>
<link rel="stylesheet" href="https://fonts.googleapis.com/css2?family=Montserrat:wght@500;800&family=Satisfy&family=Arimo:wght@400;700&display=swap">
<style>
  :root {
    --backdrop: #e8e8e8;
    --turf-green: #5e9e3c;
    --ray-green: #6aa842;
    --sun-yellow: #f7dc3a;
    --band-yellow: #f3dc2e;
    --cream: #fbf6cf;
    --ink: #4a4a44;
    --card-shadow: 0 18px 40px rgba(0, 0, 0, 0.18);
  }
  * { box-sizing: border-box; margin: 0; padding: 0; }
  html, body {
    width: 1200px;
    height: 800px;
    overflow: hidden;
    background: var(--backdrop);
  }
  .canvas {
    width: 1200px;
    height: 800px;
    display: flex;
    align-items: center;
    justify-content: center;
    gap: 60px;
  }
  .card {
    width: 490px;
    height: 280px;
    position: relative;
    overflow: hidden;
    box-shadow: var(--card-shadow);
  }

  /* Front: sunburst field with business name */
  .card-front {
    display: flex;
    align-items: center;
    justify-content: center;
  }
  .sunburst {
    position: absolute;
    inset: 0;
    background: radial-gradient(circle at 50% 48%, var(--sun-yellow) 0%, #c9d848 45%, var(--ray-green) 100%);
  }
  .brand-mark {
    position: relative;
    display: flex;
    align-items: center;
    gap: 12px;
  }
  .brand-square {
    width: 22px;
    height: 22px;
    background: var(--turf-green);
  }
  .brand-name {
    font-family: "Montserrat", sans-serif;
    font-weight: 800;
    font-size: 30px;
    letter-spacing: 1px;
    text-transform: uppercase;
    color: var(--turf-green);
  }

  /* Back: contact details */
  .card-back { background: var(--cream); }
  .title-band {
    height: 62px;
    background: var(--band-yellow);
    display: flex;
    align-items: center;
    padding-left: 30px;
  }
  .band-name {
    font-family: "Montserrat", sans-serif;
    font-weight: 800;
    font-size: 25px;
    letter-spacing: 1.5px;
    text-transform: uppercase;
    color: var(--turf-green);
  }
  .person { padding: 16px 30px 0; }
  .person-name {
    font-family: "Satisfy", cursive;
    font-size: 30px;
    color: var(--ink);
    line-height: 1.1;
  }
  .person-role {
    font-family: "Montserrat", sans-serif;
    font-weight: 500;
    font-size: 11px;
    letter-spacing: 4px;
    color: var(--turf-green);
    text-transform: uppercase;
  }
  .contact-list {
    list-style: none;
    padding: 22px 30px 0;
    font-family: "Arimo", sans-serif;
    font-size: 13px;
    color: var(--ink);
    line-height: 1.6;
  }
  .contact-label {
    display: inline-block;
    width: 20px;
    font-weight: 700;
    color: var(--turf-green);
  }
</style>
</head>
<body>
  <main class="canvas">
    <section class="card card-front">
      <div class="sunburst" role="img" aria-label="Radiating green and yellow sunburst pattern with mower mascot logo"></div>
      <div class="brand-mark">
        <span class="brand-square"></span>
        <span class="brand-name">Meadowline Turf</span>
      </div>
    </section>

    <section class="card card-back">
      <header class="title-band">
        <h1 class="band-name">Meadowline Turf</h1>
      </header>
      <div class="person">
        <p class="person-name">Gareth Pellow</p>
        <p class="person-role">Owner</p>
      </div>
      <ul class="contact-list">
        <li><span class="contact-label">T</span>0478559201</li>
        <li><span class="contact-label">E</span>meadowlineturf@mailbox-example.com</li>
        <li><span class="contact-label">W</span>www.meadowlineturf.com.au</li>
      </ul>
    </section>
  </main>
</body>
</html>
```